Need help refining Solkvartsgillet

Hi We need help with the refining of overall design and details of our homepage design Solkvartsgillet. See attached files.

Attached files:
homepage.psd - file you can use to work from.
homepage.png – quick notes on thoughts of the design
logo.psd (smart object) – The logo should be in gold.
social media elements.png - what type of data that needs design in the feed

What we need:
Something is missing with the overall design as well as detailed design for our social media feed. We don’t know what and hope you can solve this for us.

The homepage:
Our main page include a selfloading blogfeed combined with Pageloop- and Instagramfeed.

Fonts:
So far I´ve used Roboto regular, and Georgia, but feel free to use other fonts if you find better suited

Among others, we need a better detailed design that works better with the overall design.

Se attached sample image (social_mediafeed.png) what types of data we get from Pageloop in our feed. Feel free to redesign the elements of this data.

Headerlinks:
Even though we only have one page, there should be place for links to other pages as well which will load below the header.

Social media follow: Place for social media follow links/icons/buttons in style with rest of the design. Maybe at top grey border? We use Glimtora and Pageloop in style with rest of the design.

Colors:
The logo should be in gold, and use of "goldish" colors troughout the page.
Also blue elements troughout the page

Logo in gold/goldish color
Blue elements # 13416c (or similar color that works well in the design)

Target Market(s)

Wellness, fitness, spa and food, Exclusive

Number of Pages Required

1 page

Font styles to use
Serif
Sans Serif
Script
Other font styles liked:
• Roboto, Georgia

Requirements
Must have
• Better overall design that feel harmonic.
• Better design of blog and social media feeds (se all attached images)
• Nice clean design, easy on the eye
• Colors on theme: Gold + blue

```html
<!DOCTYPE html>
<html lang="sv">
<head>
<meta charset="utf-8">
<title>Solkvartsgillet</title>
<link href="https://fonts.googleapis.com/css2?family=Gelasio:wght@400;700&family=Roboto:wght@400;500;700&display=swap" rel="stylesheet">
<style>
:root{
  --blue:#13416c;
  --gold:#d9ac45;
  --gold-dark:#c99a2e;
  --ink:#2f2f2f;
  --muted:#555;
  --grey-band:#ececec;
  --grey-section:#f2f2f2;
  --footer:#333333;
  --white:#ffffff;
}
*{box-sizing:border-box;margin:0;padding:0}
html,body{width:1200px;height:3147px;overflow:hidden;background:var(--white)}
body{position:relative;font-family:"Roboto",Arial,sans-serif;color:var(--ink)}
section,header,footer,.band{position:absolute;left:0;width:1200px}

/* top bar */
.topbar{top:0;height:32px;background:var(--grey-band);font-size:13px;color:#333}
.topbar .phone{position:absolute;left:136px;top:8px;display:flex;align-items:center;gap:8px}
.topbar .account{position:absolute;right:136px;top:8px;display:flex;gap:26px}
.topbar .account span{display:flex;align-items:center;gap:7px}

/* header */
.site-header{top:32px;height:121px;background:var(--white)}
.main-nav{position:absolute;top:68px;display:flex;justify-content:space-between;border-top:1px solid var(--blue);border-bottom:1px solid var(--blue);height:24px;align-items:center;white-space:nowrap}
.main-nav a{flex:1 1 auto;text-align:center;font-family:"Gelasio",Georgia,serif;font-size:12px;color:var(--blue);text-decoration:none;padding:0 8px;border-left:1px solid var(--blue);line-height:22px;white-space:nowrap}
.main-nav a:first-child{border-left:none;flex:0 0 auto;padding-left:2px}
.main-nav a.active{color:var(--gold)}
.nav-left{left:136px;width:347px}
.nav-right{left:715px;width:349px}
.brand{position:absolute;left:500px;top:20px;width:200px;text-align:center}
.brand .mark{width:34px;height:34px;border-radius:50%;background:var(--gold);margin:0 auto 8px}
.brand .name{font-family:"Gelasio",Georgia,serif;font-size:16px;color:var(--gold);letter-spacing:1px;text-transform:uppercase;white-space:nowrap}

/* hero */
.hero{top:153px;height:467px;overflow:hidden}
.hero .photo{position:absolute;inset:0;background:linear-gradient(100deg,#dbe9f3 0%,#b7d3e6 35%,#7fb1d2 62%,#5d9cc6 100%)}
.hero .caption{position:absolute;left:150px;top:160px;width:330px}
.hero h1{font-family:"Gelasio",Georgia,serif;font-size:48px;font-weight:700;color:var(--blue);line-height:1;text-align:center;width:330px}
.hero p{font-size:24px;color:var(--blue);margin-top:14px;text-align:center;white-space:nowrap}
.hero .btn{position:absolute;left:95px;top:124px}
.dots{position:absolute;left:275px;top:360px;display:flex;gap:5px}
.dots i{width:9px;height:9px;border-radius:50%;background:#5b6670;display:block}
.dots i:first-child{background:#2c3947}

/* buttons */
.btn{display:inline-flex;align-items:center;height:36px;background:var(--blue);color:var(--white);font-size:15px;font-weight:500;padding:0 0 0 18px;width:136px;white-space:nowrap}
.btn svg{margin-left:12px}

/* section headings */
.section-title{position:absolute;left:280px;width:640px;text-align:center;border-top:2px solid #222;border-bottom:2px solid #222;height:64px;line-height:60px;font-family:"Gelasio",Georgia,serif;font-weight:400;font-size:30px;color:#222;white-space:nowrap}
.section-title em{font-style:normal;color:var(--gold)}
.section-title::before,.section-title::after{content:"";position:absolute;width:8px;height:8px;background:#222;transform:rotate(45deg);left:-4px}
.section-title::before{top:-5px}
.section-title::after{bottom:-5px}

/* offers */
.offers{top:620px;height:550px;background:var(--white)}
.offers .section-title{top:42px}
.offer-card{position:absolute;top:156px;width:286px;height:351px;border:1px solid #e8c77a;background:var(--white)}
.offer-card .photo{height:214px;background:linear-gradient(180deg,#7a5fa6 0%,#b06a98 45%,#d8876e 62%,#2c2f55 100%);position:relative}
.offer-card .photo h3{position:absolute;left:10px;top:12px;font-family:"Gelasio",Georgia,serif;color:var(--white);font-size:18px;line-height:23px;font-weight:700;white-space:nowrap}
.offer-card .badge{position:absolute;right:8px;top:8px;width:44px;height:50px;background:var(--gold);border-radius:6px 6px 22px 22px;color:var(--white);text-align:center;font-size:13px;font-weight:700;padding-top:9px;line-height:13px}
.offer-card .badge small{display:block;font-size:9px;font-weight:400}
.offer-card .company{font-size:14px;color:var(--gold);margin:20px 0 0 17px;text-transform:uppercase;letter-spacing:.3px}
.offer-card .lead{font-size:14.5px;color:#333;margin:5px 0 0 17px}
.offer-card .btn{position:absolute;left:17px;bottom:18px}

/* blog */
.blog{top:1170px;height:833px;background:var(--grey-section)}
.blog .section-title{top:40px}
.post-meta{position:absolute;top:140px;left:0;width:1200px;text-align:center;font-size:18px;color:#333;letter-spacing:.2px}
.post-meta svg{vertical-align:-2px;margin-right:6px}
.blog .photo{position:absolute;left:136px;top:190px;width:928px;height:465px;background:linear-gradient(135deg,#dfeff2 0%,#9fd3dc 30%,#4d5557 48%,#6fc2cf 65%,#bfe6ec 100%)}
.post-body{position:absolute;left:136px;top:695px;width:928px;font-size:14.5px;line-height:25px;color:#333}
.post-body .initial{float:left;font-family:"Gelasio",Georgia,serif;font-weight:700;font-size:60px;line-height:50px;margin:4px 10px 0 0;color:#222}

/* second post */
.post-two{top:2003px;height:252px;background:var(--white)}
.post-two h2{position:absolute;left:136px;top:30px;font-family:"Gelasio",Georgia,serif;font-weight:400;font-size:27px;color:#222}
.post-two p{position:absolute;left:136px;top:78px;width:928px;font-size:14.5px;line-height:25px;color:#333}
.post-two .btn{position:absolute;left:136px;top:170px}
.post-actions{position:absolute;left:296px;top:170px;height:36px;width:252px;border:1px solid #999;display:flex;align-items:center;font-size:14px;color:#333;padding-left:12px;gap:10px;white-space:nowrap}
.post-actions span{display:flex;align-items:center;gap:8px}

/* social feeds */
.feeds{top:2255px;height:592px}
.feed{position:absolute;top:0;width:600px;height:592px}
.feed.glimtora{left:0;background:var(--blue);color:var(--white)}
.feed.pageloop{left:600px;background:var(--gold);color:#1e2a3a}
.feed .icon{position:absolute;left:136px;top:34px;width:54px;height:54px;border-radius:6px;background:var(--white);opacity:.9}
.feed.pageloop .icon{left:25px;background:var(--blue)}
.feed h3{position:absolute;left:204px;top:34px;font-family:"Gelasio",Georgia,serif;font-weight:400;font-size:26px;text-transform:uppercase}
.feed .date{position:absolute;left:204px;top:72px;font-size:12.5px;text-transform:uppercase;white-space:nowrap}
.feed.pageloop h3,.feed.pageloop .date{left:93px}
.feed .photo{position:absolute;left:136px;top:120px;width:434px;height:214px}
.feed.glimtora .photo{background:linear-gradient(180deg,#9c7b54 0%,#c9b08c 45%,#eeeae4 75%,#d4cfc7 100%)}
.feed.pageloop .photo{left:25px;background:linear-gradient(180deg,#8fa6b5 0%,#c6d3d8 40%,#e6d7b8 65%,#9b8e80 100%)}
.feed .text{position:absolute;left:136px;top:357px;width:434px;font-size:14px;line-height:22px}
.feed.pageloop .text{left:25px;color:var(--blue)}
.feed .tags{position:absolute;left:136px;top:447px;width:434px;font-size:14px;line-height:25px}

/* footer */
.site-footer{top:2847px;height:254px;background:var(--footer);color:#eee}
.f-col{position:absolute;top:0;height:220px;padding-top:42px}
.f-col h4{font-family:"Gelasio",Georgia,serif;font-size:18px;font-weight:700;color:var(--white);margin-bottom:20px}
.f-col.links{left:136px;width:200px}
.f-col.contact{left:361px;width:280px}
.f-col.inquiry{left:667px;width:280px}
.f-col.follow{left:976px;width:130px}
.f-rule{position:absolute;top:40px;width:1px;height:160px;background:#4a4a4a}
.f-col ul{list-style:none;font-size:12.5px}
.f-col.links li{margin-bottom:8px;padding-left:18px;position:relative}
.f-col.links li::before{content:"";position:absolute;left:3px;top:6px;width:5px;height:5px;border-radius:50%;background:#eee}
.f-col.contact li{display:flex;gap:12px;margin-bottom:12px;line-height:15px;font-size:12px}
.f-col.contact li svg{flex:none;margin-top:1px}
.field{width:235px;height:24px;background:var(--white);color:#333;font-size:11px;padding:5px 6px;margin-bottom:4px}
.field.msg{height:42px}
.submit{display:inline-block;margin-top:6px;background:var(--gold);color:#1e1e1e;font-weight:700;font-size:15px;padding:6px 20px}
.f-col.follow li{display:flex;align-items:center;gap:12px;margin-bottom:18px;font-size:12px}
.f-col.follow li i{width:18px;height:18px;background:#eee;display:block;border-radius:2px}
.copyright{top:3101px;height:46px;background:var(--gold);text-align:center;font-size:14px;line-height:46px;color:#2a2a2a}
</style>
</head>
<body>

<div class="band topbar">
  <div class="phone">
    <svg width="16" height="16" viewBox="0 0 16 16"><circle cx="8" cy="8" r="7.2" fill="none" stroke="#333" stroke-width="1.2"/><path d="M5.3 4.3c.4-.3.9-.3 1.1.1l.7 1.2c.2.4 0 .7-.3 1l-.4.3c.4.9 1.1 1.6 2 2l.3-.4c.3-.3.6-.5 1-.3l1.2.7c.4.2.4.7.1 1.1-.6.8-1.5 1-2.5.5-1.7-.8-3-2.1-3.8-3.8-.5-1-.3-1.900.6-2.400z" fill="#333"/></svg>
    012-555-0147
  </div>
  <div class="account">
    <span><svg width="18" height="16" viewBox="0 0 18 16"><rect x="1" y="3" width="16" height="11" rx="1" fill="none" stroke="#333" stroke-width="1.3"/><path d="M6 3V1h6v2" fill="none" stroke="#333" stroke-width="1.3"/></svg>Bli medlem</span>
    <span><svg width="16" height="16" viewBox="0 0 16 16"><circle cx="8" cy="8" r="7.2" fill="none" stroke="#333" stroke-width="1.2"/><circle cx="8" cy="6.5" r="2.4" fill="none" stroke="#333" stroke-width="1.2"/><path d="M3.6 13c1-2 2.6-3 4.4-3s3.4 1 4.4 3" fill="none" stroke="#333" stroke-width="1.2"/></svg>Medlemslogin</span>
  </div>
</div>

<header class="site-header">
  <nav class="main-nav nav-left">
    <a class="active" href="#">HEM</a>
    <a href="#">SOLKVARTSRESOR</a>
    <a href="#">INSPIRATION</a>
  </nav>
  <div class="brand">
    <div class="mark"></div>
    <div class="name">Solkvartsgillet</div>
  </div>
  <nav class="main-nav nav-right">
    <a href="#">MEDLEMSERBJUDANDEN</a>
    <a href="#">OM &#9662;</a>
    <a href="#">KONTAKTA OSS</a>
  </nav>
</header>

<section class="hero">
  <div class="photo" role="img" aria-label="Kvinna i baddräkt sitter i ljusblått vatten, pastellblå himmel"></div>
  <div class="caption">
    <h1>Featured</h1>
    <p>Liten Beskrivning av Post</p>
    <span class="btn">LÄS MER
      <svg width="22" height="26" viewBox="0 0 22 26"><path d="M2 2h18v11c0 6-5 9-9 11C7 22 2 19 2 13z" fill="#fff" stroke="#d9ac45" stroke-width="1.5"/><path d="M8 8l7 5-7 5z" fill="#d9ac45"/></svg>
    </span>
  </div>
  <div class="dots"><i></i><i></i><i></i><i></i></div>
</section>

<section class="offers">
  <h2 class="section-title">Solkvartsgillets <em>Medlemserbjudanden</em></h2>

  <article class="offer-card" style="left:136px">
    <div class="photo" role="img" aria-label="Kvällsvy över en upplyst kuststad i lila skymning">
      <h3>Ljus &amp; Balans AB<br>Motionera Mera</h3>
      <div class="badge">30%<small>Rabatt</small></div>
    </div>
    <p class="company">Ljus &amp; Balans AB</p>
    <p class="lead">En kort rubrik på erbjudandet</p>
    <span class="btn">LÄS MER
      <svg width="22" height="26" viewBox="0 0 22 26"><path d="M2 2h18v11c0 6-5 9-9 11C7 22 2 19 2 13z" fill="#fff" stroke="#d9ac45" stroke-width="1.5"/><path d="M8 8l7 5-7 5z" fill="#d9ac45"/></svg>
    </span>
  </article>

  <article class="offer-card" style="left:457px">
    <div class="photo" role="img" aria-label="Kvällsvy över en upplyst kuststad i lila skymning">
      <h3>Ljus &amp; Balans AB<br>Motionera Mera</h3>
      <div class="badge">30%<small>Rabatt</small></div>
    </div>
    <p class="company">Ljus &amp; Balans AB</p>
    <p class="lead">En kort rubrik på erbjudandet</p>
    <span class="btn">LÄS MER
      <svg width="22" height="26" viewBox="0 0 22 26"><path d="M2 2h18v11c0 6-5 9-9 11C7 22 2 19 2 13z" fill="#fff" stroke="#d9ac45" stroke-width="1.5"/><path d="M8 8l7 5-7 5z" fill="#d9ac45"/></svg>
    </span>
  </article>

  <article class="offer-card" style="left:778px">
    <div class="photo" role="img" aria-label="Kvällsvy över en upplyst kuststad i lila skymning">
      <h3>Ljus &amp; Balans AB<br>Motionera Mera</h3>
      <div class="badge">30%<small>Rabatt</small></div>
    </div>
    <p class="company">Ljus &amp; Balans AB</p>
    <p class="lead">En kort rubrik på erbjudandet</p>
    <span class="btn">LÄS MER
      <svg width="22" height="26" viewBox="0 0 22 26"><path d="M2 2h18v11c0 6-5 9-9 11C7 22 2 19 2 13z" fill="#fff" stroke="#d9ac45" stroke-width="1.5"/><path d="M8 8l7 5-7 5z" fill="#d9ac45"/></svg>
    </span>
  </article>
</section>

<section class="blog">
  <h2 class="section-title">En trevlig rubrik <em>på ditt blogginlägg</em></h2>
  <p class="post-meta">22 OKTOBER, 2016 | AV SOLKVARTSGILLET | 0 KOMMENTARER |
    <svg width="15" height="15" viewBox="0 0 15 15"><path d="M1 1h6l7 7-6 6-7-7z" fill="#d9ac45"/><circle cx="4.5" cy="4.5" r="1.3" fill="#fff"/></svg>SPA, LIVSNJUTNING, YOGA</p>
  <div class="photo" role="img" aria-label="Kvinna i vit bikini vid en turkos geotermisk lagun med mörka lavaklippor"></div>
  <div class="post-body">
    <span class="initial">E</span>Sed dui consectetur, eleifend nibh et, ultricies justo. Vivamus luctus elit ac lacus placerat laoreet vel at lacus. Sed a molestie ex. Vestibulum ac varius libero. Fusce sollicitudin non tellus lacinia molestie. Sed rhoncus dui a sem accumsan, nec scelerisque augue suscipit. Aliquam eget justo odio. Maecenas in molestie tortor, eu tristique ligula. Suspendisse vulputate urna ut elit iacul varius.
  </div>
</section>

<section class="post-two">
  <h2>Rubrik 2</h2>
  <p>Quisque laoreet nisi purus. Suspendisse sit amet nulla dolor. Morbi felis sem, condimentum fermentum ullamcorper a, auctor rhoncus justo. Morbi tempus sit amet ante eu placerat. In nec odio ac dui molestie iaculis eu nec tellus. Etiam venenatis sed dolor in commodo. Sed venenatis iaculis faucibus. Quisque eleifend a leo eu sodales.</p>
  <span class="btn">LÄS MER
    <svg width="22" height="26" viewBox="0 0 22 26"><path d="M2 2h18v11c0 6-5 9-9 11C7 22 2 19 2 13z" fill="#fff" stroke="#d9ac45" stroke-width="1.5"/><path d="M8 8l7 5-7 5z" fill="#d9ac45"/></svg>
  </span>
  <div class="post-actions">
    <span><svg width="16" height="16" viewBox="0 0 16 16"><circle cx="12" cy="3.5" r="2.3" fill="none" stroke="#d9ac45" stroke-width="1.4"/><circle cx="4" cy="8" r="2.3" fill="none" stroke="#d9ac45" stroke-width="1.4"/><circle cx="12" cy="12.5" r="2.3" fill="none" stroke="#d9ac45" stroke-width="1.4"/><path d="M6 7l4-2.4M6 9l4 2.4" stroke="#d9ac45" stroke-width="1.4"/></svg>DELA</span>
    <span>|</span>
    <span><svg width="18" height="16" viewBox="0 0 18 16"><path d="M1 1h16v10H7l-4 4v-4H1z" fill="#d9ac45"/></svg>KOMMENTERA</span>
  </div>
</section>

<section class="feeds">
  <div class="feed glimtora">
    <div class="icon"></div>
    <h3>Glimtora</h3>
    <p class="date">15 oktober, 2016 | av Solkvartsgillet</p>
    <div class="photo" role="img" aria-label="Ljust hotellrum med bäddad dubbelsäng och vägglampor"></div>
    <p class="text">Ni vet den där känslan när man kommer in på hotellrummet för första gången och vet att man är långledig tillsammans hela helgen. Den känslan...</p>
    <p class="tags">#långledig #välmående #momentsofhappiness #solkvartsvän #solkvartsgillet</p>
  </div>
  <div class="feed pageloop">
    <div class="icon"></div>
    <h3>Pageloop</h3>
    <p class="date">15 oktober, 2016 | av Solkvartsgillet</p>
    <div class="photo" role="img" aria-label="Två glas med varmt ingefärsvatten och citronskivor vid havet"></div>
    <p class="text">Boosta ditt immunförsvar!<br>Skiva ingefära och citron och häll hett vatten över. Ingefära är kroppens bästa vän som ökar både blodcirkulation och ämnesomsättningen. Den är antiinflammatorisk och motverkar både migrän och problem med lederna. Citron renar kroppen på gifter, stärker immunförsvaret, renar huden och ger energi. Denna välgörande dryck är full av antioxidanter som stärker kroppen. En god morgonvana för att boosta det friska.</p>
  </div>
</section>

<footer class="site-footer">
  <div class="f-col links">
    <h4>Quick Links</h4>
    <ul>
      <li>Hem</li><li>Solkvartsresor</li><li>Inspiration</li><li>Medlemserbjudanden</li><li>Om</li><li>Kontakta Oss</li>
    </ul>
  </div>
  <div class="f-rule" style="left:340px"></div>
  <div class="f-col contact">
    <h4>Contact Details</h4>
    <ul>
      <li><svg width="12" height="14" viewBox="0 0 12 14"><path d="M6 0a5 5 0 015 5c0 3.5-5 9-5 9S1 8.5 1 5a5 5 0 015-5z" fill="#eee"/><circle cx="6" cy="5" r="1.8" fill="#333"/></svg><span>Solgatan 5, ljus och lugn vid vattnet<br>Kvartsvägen 12, Postnr: 897 41</span></li>
      <li><svg width="12" height="12" viewBox="0 0 12 12"><path d="M2 .5c.5-.4 1.1-.3 1.4.2l.9 1.5c.3.5.1.9-.3 1.2l-.5.4c.6 1.2 1.5 2.1 2.7 2.7l.4-.5c.3-.4.7-.6 1.2-.3l1.5.9c.5.3.6.9.2 1.4-.8 1-2 1.3-3.3.6C4.2 7.6 2.5 5.9 1.5 3.8.8 2.5 1 1.3 2 .5z" fill="#eee"/></svg>012-555-0147</li>
      <li><svg width="14" height="12" viewBox="0 0 14 12"><rect x="0" y="4" width="14" height="8" rx="1" fill="#eee"/><rect x="3" y="0" width="8" height="5" fill="#eee"/><rect x="4" y="7" width="6" height="3" fill="#333"/></svg>012-555-0148</li>
      <li><svg width="14" height="11" viewBox="0 0 14 11"><rect x="0" y="0" width="14" height="11" rx="1" fill="#eee"/><path d="M1 1l6 5 6-5" fill="none" stroke="#333" stroke-width="1.2"/></svg>hej@solkvartsgillet.example</li>
    </ul>
  </div>
  <div class="f-rule" style="left:645px"></div>
  <div class="f-col inquiry">
    <h4>Quick Inquiry</h4>
    <div class="field">Your Name</div>
    <div class="field">Email</div>
    <div class="field msg">Message</div>
    <span class="submit">SUBMIT</span>
  </div>
  <div class="f-rule" style="left:950px"></div>
  <div class="f-col follow">
    <h4>Follow Us</h4>
    <ul>
      <li><i></i>Pageloop</li>
      <li><i></i>Kvittra</li>
      <li><i></i>Cirkelnet</li>
      <li><i></i>Yrkeslänk</li>
    </ul>
  </div>
</footer>

<div class="band copyright">Copyright © 2016 SOLKVARTSGILLET &nbsp;|&nbsp; All rights reserved</div>

</body>
</html>
```